Büro Vermietung
Velbrin Design Studio hat eine super Arbeit abgeliefert. Wir sind sehr zufrieden mit der Arbeit und natürlich mit dem Design.
Zielgruppe
Bitte keine weiteren Vorschläge mehr. - Wir haben uns bereits für ein Projekte entschieden.
Aufgabenstellung
Interessenten, welche sich für die Büros oder Gewerbefläche interessieren, sollten auf der Webpage folgende Informationen vorfinden:
Menü-Leiste:
HOME / FLÄCHEN / BILDER / LAGE / KONTAKT
HOME:
Titelbild mit dem Hund & weitblick-raeume.ch + Frontbild Liegenschaft
(Zusatztext folgt noch)
FLAECHEN:
Grundriss & Preise
BILDER:
diverse Bilder (folgen noch)
LAGE:
KONTAKT:
(Unsere Adresse) Vermieter /Kontakt
KARELU IMMOBILEN AG

```html
<!DOCTYPE html>
<html lang="de">
<head>
<meta charset="utf-8">
<title>Büro Vermietung – weitblick-raeume.ch</title>
<link rel="stylesheet" href="https://fonts.googleapis.com/css2?family=Encode+Sans+Condensed:wght@300;400;500;600&display=swap">
<style>
:root{
  --teal:#2ba3c6;
  --green:#8eae3c;
  --navy:#133c5e;
  --text:#3c3c3c;
  --line:#b9c2cf;
  --band-light:#f4f4f4;
  --band-grey:#c3cad5;
  --white:#ffffff;
}
*{box-sizing:border-box;margin:0;padding:0}
html,body{width:1200px;height:4294px;overflow:hidden}
body{position:relative;font-family:"Encode Sans Condensed",sans-serif;font-weight:300;color:var(--text);background:var(--white)}
.abs{position:absolute}
.hero-bg{left:0;top:0;width:1200px;height:875px;background:linear-gradient(90deg,#c4cbd6 0%,#e6e9ee 30%,#fbfbfc 52%,#e6e9ee 72%,#c4cbd6 100%)}
.card{background:var(--white)}
.brand-card{left:60px;top:0;width:303px;height:645px}
.mascot{left:20px;top:20px;width:263px;height:195px;background:radial-gradient(circle at 50% 45%,#e9dfd2 0%,#f6f2ec 55%,#ffffff 80%)}
.site-name{left:0;top:222px;width:303px;text-align:center;font-size:33px;font-weight:400;color:var(--teal);letter-spacing:-0.5px}
.offer-title{left:12px;top:455px;font-size:34px;font-weight:500;color:var(--green)}
.offer-address{left:12px;top:505px;font-size:20px;display:flex;align-items:center;gap:10px}
.facts{left:12px;top:540px;width:230px;font-size:18px;line-height:23px}
.facts div{display:flex;justify-content:space-between}
.topbar{left:385px;top:0;width:755px;height:92px;background:var(--white)}
.nav-brand{left:16px;top:50px;font-size:17px;font-weight:600;color:var(--navy);display:flex;align-items:center;gap:5px}
.nav-brand i{display:block;width:12px;height:12px;background:var(--navy)}
.nav{right:18px;top:51px;display:flex;gap:20px;font-size:20px;color:#333}
.nav .active{color:var(--teal)}
.photo-card{left:385px;top:113px;width:755px;height:532px}
.photo-card .img{left:17px;top:20px;width:721px;height:495px;background:linear-gradient(180deg,#2f63c8 0%,#6b97dc 40%,#dfe4ea 62%,#7b8a7c 85%,#4a5a3e 100%)}
.thumb{top:683px;width:345px;height:159px}
.thumb .img{left:15px;top:17px;width:314px;height:124px;background:linear-gradient(180deg,#f2f2f2 0%,#e3e5e3 55%,#c9d89a 80%,#d6d6d6 100%)}
.band-pattern{left:0;width:1200px;background:#ececec}
.band-title{left:0;width:1200px;background:var(--band-light);display:flex;align-items:center;justify-content:center;flex-direction:column}
.band-title h2{font-size:34px;font-weight:500;color:var(--teal)}
.band-title p{font-size:17px;font-weight:500;color:var(--teal);margin-top:6px}
.band-grad{left:0;width:1200px;background:linear-gradient(90deg,#b9c2cf 0%,#e4e7ec 35%,#fafafb 50%,#e4e7ec 65%,#b9c2cf 100%)}
.text-card{left:62px;top:1122px;width:560px;height:561px;padding:14px 22px;font-size:16px;line-height:20px}
.text-card p{margin-bottom:21px}
.text-card .gap{margin-top:40px}
.facts-small{width:180px;font-size:16px;line-height:20px}
.facts-small div{display:flex;justify-content:space-between}
.plan-card{left:645px;top:1122px;width:497px;height:486px;font-size:16px;line-height:20px}
.plan-card .img{left:15px;top:28px;width:467px;height:292px;background:linear-gradient(160deg,#eef0ee 0%,#d8dcd6 50%,#c3c8c2 100%)}
.plan-link{left:14px;top:362px}
.plan-link span{color:var(--teal)}
.plan-note{left:14px;top:424px}
.btn{display:flex;align-items:center;justify-content:center;border:2px solid var(--navy);border-radius:3px;background:var(--white);font-size:16px;font-weight:600;color:var(--navy);letter-spacing:0.3px}
.btn-termin{left:645px;top:1637px;width:272px;height:44px}
.gallery-bg{left:0;top:1992px;width:1200px;height:628px;background:linear-gradient(90deg,#c3cad5 0%,#e9ecf0 30%,#fbfbfc 50%,#e9ecf0 70%,#c3cad5 100%)}
.gallery-main{left:60px;top:2075px;width:615px;height:463px;background:linear-gradient(90deg,#1d3463 0%,#33476b 12%,#e4e6e0 30%,#f1f1ec 60%,#dcdcd6 100%)}
.gallery-thumb{width:147px;height:110px;background:linear-gradient(90deg,#1d3463 0%,#2f4670 18%,#e1e4dc 40%,#eeeee8 100%)}
.btn-expose{left:867px;top:2493px;width:273px;height:45px}
.map-strip{left:0;top:2620px;width:1200px;height:113px;background:linear-gradient(180deg,#eceae4 0%,#e3e1da 50%,#dcdfe4 100%)}
.map{left:0;top:2863px;width:1200px;height:629px;background:linear-gradient(135deg,#ebe8e1 0%,#e5e2da 45%,#dfdcd3 100%)}
.contact-head{left:60px;top:3730px;font-size:33px;font-weight:300;color:var(--teal);line-height:31px}
.field{left:60px;width:312px;height:32px;border:1px solid #c9a7b0;border-radius:3px;font-size:11px;color:#999;padding:8px 6px}
.field-msg{left:403px;top:3910px;width:359px;height:165px;border:1px solid #b9b9b9;border-radius:3px;font-size:11px;color:#999;padding:8px 8px}
.btn-send{left:510px;top:4113px;width:252px;height:45px;border:1px solid #444;border-radius:3px;display:flex;align-items:center;justify-content:center;font-size:18px;color:#333}
.company-mark{left:880px;top:3935px;font-size:34px;font-weight:600;color:var(--navy);display:flex;align-items:center;gap:8px}
.company-mark i{display:block;width:30px;height:30px;background:var(--navy)}
.company-info{left:882px;top:4000px;font-size:16px;line-height:20px}
.company-info b{font-weight:600}
.footer{left:0;top:4230px;width:1200px;height:64px;background:var(--navy)}
.footer span{position:absolute;right:48px;top:22px;font-size:14px;color:var(--white)}
</style>
</head>
<body>

<div class="abs hero-bg"></div>

<div class="abs card brand-card">
  <div class="abs mascot" role="img" aria-label="Illustration eines Hundes mit Brille am Schreibtisch"></div>
  <div class="abs site-name">WEITBLICK-RAEUME.CH</div>
  <h1 class="abs offer-title">BÜRO VERMIETUNG</h1>
  <div class="abs offer-address">Lindenweg 28, 5000 Aarau
    <svg width="18" height="18" viewBox="0 0 18 18"><circle cx="7" cy="7" r="5" fill="none" stroke="#aaa" stroke-width="1.6"/><line x1="11" y1="11" x2="16" y2="16" stroke="#aaa" stroke-width="2"/></svg>
  </div>
  <div class="abs facts">
    <div><span>Fläche:</span><span>1100 m²</span></div>
    <div><span>Miete/Monat:</span><span>8.000,00 CHF</span></div>
    <div><span>Nebenkosten:</span><span>500,00 CHF</span></div>
    <div><span>Parkplätze:</span><span>25</span></div>
  </div>
</div>

<div class="abs topbar">
  <div class="abs nav-brand"><i></i>KARELU</div>
  <nav class="abs nav"><span class="active">STARTSEITE</span><span>FLAECHEN</span><span>BILDER</span><span>LAGE</span><span>KONTAKT</span></nav>
</div>

<div class="abs card photo-card">
  <div class="abs img" role="img" aria-label="Foto des Bürogebäudes unter blauem Himmel"></div>
</div>

<div class="abs card thumb" style="left:62px"><div class="abs img" role="img" aria-label="Visualisierung Büro mit Arbeitsplätzen"></div></div>
<div class="abs card thumb" style="left:428px"><div class="abs img" role="img" aria-label="Visualisierung Sitzungszimmer"></div></div>
<div class="abs card thumb" style="left:795px"><div class="abs img" role="img" aria-label="Visualisierung Büro mit Aktenregalen"></div></div>

<div class="abs band-pattern" style="top:875px;height:88px"></div>
<div class="abs band-title" style="top:963px;height:129px"><h2>FLAECHEN / PREISE</h2></div>
<div class="abs band-pattern" style="top:1092px;height:655px"></div>

<div class="abs card text-card">
  <p>Ob Büro, Praxis, Schulungsräume oder Atelier, hier kann ganz auf Ihre Wünsche eingegangen werden. Selbst für Gastronomiebetriebe eignen sich die attraktiven Flächen.</p>
  <p>Im Obergeschoss steht ein besonderes Schmankerl bereit. Der wunderschöne, lichtdurchflutete Raum hat den Charakter eines Penthouses und der große Balkon gibt dem Ganzen eine exklusive Note.</p>
  <p>Für Fitnessstudios, vielleicht sogar mit Wellnessbereich, sind die Räumlichkeiten wie geschaffen.</p>
  <p>Benötigen Sie zusätzlich Lagerflächen?<br>Kein Problem, im Untergeschoss ist auch das verfügbar.</p>
  <p>Parkplätze in ausreichender Anzahl sind vorhanden.</p>
  <p class="gap">Schauen Sie sich diese schönen Räume an und entscheiden Sie dann, über den Mietpreis lässt sich ganz sicher eine Einigung erzielen.</p>
  <p style="margin-top:40px">Für das Gebäude liegt uns zur Zeit noch kein Energieausweis vor.</p>
  <div class="facts-small">
    <div><span>Fläche:</span><span>1100 m²</span></div>
    <div><span>Miete/Monat:</span><span>8.000,00 CHF</span></div>
    <div><span>Nebenkosten:</span><span>500,00 CHF</span></div>
    <div><span>Parkplätze:</span><span>25</span></div>
  </div>
</div>

<div class="abs card plan-card">
  <div class="abs img" role="img" aria-label="3D-Grundriss der Bürofläche mit Arbeitsplätzen"></div>
  <div class="abs plan-link"><span>»</span> Hier gehts zum Grundriss</div>
  <div class="abs plan-note">Sie haben Interesse an diesem einzigartigen Mietangebot?<br>Wir freuen uns auf Sie!</div>
</div>
<div class="abs btn btn-termin">JETZT TERMIN VEREINBAREN</div>

<div class="abs band-grad" style="top:1747px;height:120px"></div>
<div class="abs band-title" style="top:1867px;height:125px"><h2>IMPRESSIONEN</h2></div>

<div class="abs gallery-bg"></div>
<div class="abs gallery-main" role="img" aria-label="Foto eines leeren Büroraums mit Glastür"></div>
<div class="abs gallery-thumb" style="left:683px;top:2075px" role="img" aria-label="Bürofoto"></div>
<div class="abs gallery-thumb" style="left:837px;top:2075px" role="img" aria-label="Bürofoto"></div>
<div class="abs gallery-thumb" style="left:993px;top:2075px" role="img" aria-label="Bürofoto"></div>
<div class="abs gallery-thumb" style="left:683px;top:2193px" role="img" aria-label="Bürofoto"></div>
<div class="abs gallery-thumb" style="left:837px;top:2193px" role="img" aria-label="Bürofoto"></div>
<div class="abs gallery-thumb" style="left:993px;top:2193px" role="img" aria-label="Bürofoto"></div>
<div class="abs gallery-thumb" style="left:683px;top:2311px" role="img" aria-label="Bürofoto"></div>
<div class="abs gallery-thumb" style="left:837px;top:2311px" role="img" aria-label="Bürofoto"></div>
<div class="abs gallery-thumb" style="left:993px;top:2311px" role="img" aria-label="Bürofoto"></div>
<div class="abs btn btn-expose">EXPOSEE HERUNTERLADEN</div>

<div class="abs map-strip" role="img" aria-label="Kartenausschnitt mit Flusslauf"></div>
<div class="abs band-title" style="top:2733px;height:130px"><h2>LAGE</h2><p>Lindenweg 28, CH-5000 Aarau</p></div>
<div class="abs map" role="img" aria-label="Stadtplan mit Standortmarkierung des Gebäudes"></div>

<div class="abs contact-head">TRETEN SIE MIT UNS IN KONTAKT.<br>WIR FREUEN UNS AUF SIE.</div>

<div class="abs field" style="top:3910px">FIRMA</div>
<div class="abs field" style="top:3955px">NAME</div>
<div class="abs field" style="top:4000px">TELEFON</div>
<div class="abs field" style="top:4045px">EMAIL</div>
<div class="abs field-msg">NACHRICHT</div>
<div class="abs btn-send">ABSENDEN</div>

<div class="abs company-mark"><i></i>KARELU</div>
<div class="abs company-info">
  <b>KARELU IMMOBILEN AG</b><br>
  Birkenstrasse 12 | 8004 Zürich<br><br>
  Tel: 044 555 01 23 | info@karelu-immo.ch
</div>

<div class="abs footer"><span>Impressum</span></div>

</body>
</html>
```